Real Estate Website

Peckford Realty will primarily be a residential rental and sales business.

Sales - Current properties - sold properties
Rentals - current properties - leased properties
Insights - Blog - Suburb profile
About us - Our agents
Working with us - rental/Sales

Here is a site that i like. Dont require video in the background.
https://www.mintowgate.com.au/
Scaled down version of this would be great. I like the landing page where it focuses on the client being vendor/landlord - not the buyers and sellers

Please make a banner on the home page that says 'request a free appraisal' with a button saying 'click here'.

I've attached some branding logos etc.
Brand colour is #f6ecd7 but using a white or black as the main of the website is fine.

```html
<!DOCTYPE html>
<html lang="en">
<head>
<meta charset="utf-8">
<title>Peckford Realty</title>
<link href="https://fonts.googleapis.com/css2?family=Nunito:wght@400;600;700;800&family=Exo+2:wght@400;500&family=Oswald:wght@500&display=swap" rel="stylesheet">
<style>
:root{
  --ink:#111111;
  --text:#2b2b2b;
  --white:#ffffff;
  --brand:#f6ecd7;
  --gold:#f2c46b;
  --tan:#f3e2c3;
  --footer:#000000;
  --line:#8a8a8a;
}
*{margin:0;padding:0;box-sizing:border-box}
html,body{width:1200px;height:3843px;overflow:hidden}
body{position:relative;background:var(--white);color:var(--text);font-family:"Nunito",sans-serif}
.abs{position:absolute}

/* header */
.site-header{position:absolute;left:0;top:0;width:1200px;height:96px;background:var(--white)}
.brand-name{position:absolute;left:110px;top:26px;text-align:center;font-family:"Nunito",sans-serif;font-weight:600;color:var(--ink);line-height:1}
.brand-name .top{display:block;font-size:29px;letter-spacing:2px}
.brand-name .bottom{display:block;font-size:19px;letter-spacing:3px;margin-top:2px}
.main-nav{position:absolute;top:36px;left:316px;display:flex;gap:0;font-size:16px;color:var(--ink)}
.main-nav a{color:inherit;text-decoration:none;position:absolute;white-space:nowrap}
.phone-link{position:absolute;left:930px;top:23px;display:flex;align-items:center;gap:12px;font-size:16px;color:var(--ink)}
.phone-circle{width:47px;height:47px;border:2px solid var(--ink);border-radius:50%;display:flex;align-items:center;justify-content:center}

/* hero */
.hero{position:absolute;left:0;top:96px;width:1200px;height:556px;background:linear-gradient(180deg,#4a5563 0%,#6b6f74 35%,#8a7c62 58%,#3e4a2c 85%,#2f3a22 100%)}
.hero-title{position:absolute;left:0;width:1200px;top:302px;text-align:center;font-family:"Nunito",sans-serif;font-weight:600;font-size:43px;color:var(--white);letter-spacing:.5px}
.hero-btn{position:absolute;left:522px;top:383px;width:142px;height:48px;background:var(--white);border-radius:3px;display:flex;align-items:center;justify-content:center;font-size:15px;color:var(--ink)}

/* about */
.about-accent{position:absolute;left:134px;top:786px;width:30px;height:344px;background:var(--tan)}
.about-photo{position:absolute;left:151px;top:740px;width:346px;height:458px;background:linear-gradient(160deg,#c9ab86 0%,#8f7560 45%,#5f6b7c 100%);box-shadow:0 4px 14px rgba(0,0,0,.25)}
.about-title{position:absolute;left:548px;top:802px;font-size:36px;font-weight:700;color:var(--ink);letter-spacing:1px}
.about-text{position:absolute;left:548px;top:862px;width:510px;font-size:15px;line-height:27.4px;color:var(--text)}
.btn-tan{position:absolute;left:548px;top:1076px;width:127px;height:54px;background:var(--tan);display:flex;align-items:center;justify-content:center;font-size:15px;color:var(--ink);letter-spacing:.3px}

/* working with us */
.working{position:absolute;left:0;top:1288px;width:1200px;height:825px;background:var(--brand)}
.section-title{position:absolute;left:0;width:1200px;text-align:center;font-size:36px;font-weight:800;color:var(--ink);letter-spacing:.5px}
.working-intro{position:absolute;left:250px;width:700px;top:105px;text-align:center;font-size:15px;line-height:28px}
.tab{position:absolute;top:185px;height:36px;background:var(--tan);display:flex;align-items:center;justify-content:center;font-size:18px;color:var(--ink);letter-spacing:.5px}
.listing-card{position:absolute;top:288px;width:308px;height:457px;background:var(--white);box-shadow:0 2px 6px rgba(0,0,0,.08)}
.listing-photo{position:absolute;left:0;top:0;width:308px;height:220px}
.badge{position:absolute;top:10px;height:26px;padding:0 9px;font-family:"Exo 2",sans-serif;font-size:15px;display:flex;align-items:center;color:var(--ink)}
.badge.type{background:var(--gold)}
.badge.new{background:var(--white)}
.listing-title{position:absolute;left:12px;top:240px;font-family:"Exo 2",sans-serif;font-weight:500;font-size:19px;color:var(--ink)}
.listing-price{position:absolute;left:15px;top:276px;font-family:"Exo 2",sans-serif;font-size:17px;color:var(--ink)}
.listing-desc{position:absolute;left:17px;top:309px;width:280px;font-family:"Exo 2",sans-serif;font-size:15px;line-height:28px}
.listing-specs{position:absolute;left:19px;top:408px;display:flex;align-items:center;gap:8px;font-family:"Exo 2",sans-serif;font-size:15px;color:var(--ink)}
.listing-specs span{margin-right:8px}

/* insights */
.insight{position:absolute;width:380px}
.insight-photo{width:380px;height:298px}
.insight-label{position:absolute;left:2px;top:325px;font-size:15px;font-weight:600;color:var(--ink)}
.insight-title{position:absolute;left:2px;top:358px;font-size:23px;font-weight:700;color:var(--ink);letter-spacing:.3px}
.insight-text{position:absolute;left:3px;top:401px;width:320px;font-size:13px;line-height:24px}
.insight-price{position:absolute;left:3px;top:510px;font-size:21px;font-weight:700;color:var(--ink)}

/* footer */
.site-footer{position:absolute;left:0;top:3481px;width:1200px;height:362px;background:var(--footer);color:var(--white)}
.footer-heading{position:absolute;top:84px;font-family:"Oswald",sans-serif;font-weight:500;font-size:14px;line-height:22px;letter-spacing:.2px}
.footer-contact{position:absolute;left:178px;top:148px;font-size:14px;line-height:25px}
.copyright{position:absolute;left:176px;top:242px;font-size:13px}
.field{position:absolute;border:1px solid var(--line);font-size:14px;color:var(--white);padding:4px 11px}
.submit{position:absolute;left:960px;top:270px;width:62px;text-align:right;font-family:"Oswald",sans-serif;font-size:14px}
</style>
</head>
<body>

<header class="site-header">
  <div class="brand-name"><span class="top">PECKFORD</span><span class="bottom">REALTY</span></div>
  <nav class="main-nav">
    <a style="left:0">Home</a>
    <a style="left:82px">Sales</a>
    <a style="left:160px">Rentals</a>
    <a style="left:255px">Insights</a>
    <a style="left:353px">About us</a>
    <a style="left:456px">Working with us</a>
  </nav>
  <div class="phone-link">
    <span class="phone-circle">
      <svg width="16" height="16" viewBox="0 0 24 24"><path fill="#111" d="M6.6 10.8a15.1 15.1 0 0 0 6.6 6.6l2.2-2.2c.3-.3.7-.4 1-.2 1.1.4 2.3.6 3.6.6.6 0 1 .4 1 1V20c0 .6-.4 1-1 1A17 17 0 0 1 3 4c0-.6.4-1 1-1h3.5c.6 0 1 .4 1 1 0 1.3.2 2.5.6 3.6.1.3 0 .7-.2 1z"/></svg>
    </span>
    <span>188-555-014</span>
  </div>
</header>

<section class="hero" role="img" aria-label="Modern two-storey house at dusk with warmly lit windows on a green lawn">
  <h1 class="hero-title">REQUEST A FREE APPRAISAL</h1>
  <div class="hero-btn">CLICK HERE</div>
</section>

<section>
  <div class="about-accent"></div>
  <div class="about-photo" role="img" aria-label="Smiling family sitting on the floor under a cardboard roof, holding a potted plant"></div>
  <h2 class="about-title">ABOUT US</h2>
  <p class="about-text">Lorem ipsum dolor sit amet, consectetur adipiscing elit, sed do eiusmod tempor incididunt ut labore et dolore magna aliqua. Ut enim ad minim veniam, quis nostrud exercitation ullamco laboris nisi ut aliquip ex ea commodo consequat.Duis aute irure dolor in reprehenderit in voluptate velit esse cillum dolore eu fugiat nulla pariatur. Excepteur sint occaecat cupidatat non proident, sunt in culpa qui officia deserunt mollit anim id est laborum."</p>
  <div class="btn-tan">LAERN MORE</div>
</section>

<section class="working">
  <h2 class="section-title" style="top:44px">WORKING WITH US</h2>
  <p class="working-intro">Lorem ipsum dolor sit amet, consectetur adipiscing elit, sed do eiusmod tempor incididunt ut labore et dolore magna aliqua.</p>
  <div class="tab" style="left:433px;width:91px">SALES</div>
  <div class="tab" style="left:542px;width:115px">RENTALS</div>
  <div class="tab" style="left:676px;width:91px">SOLD</div>

  <article class="listing-card" style="left:112px">
    <div class="listing-photo" role="img" aria-label="Single-storey house with grey roof and landscaped front garden" style="background:linear-gradient(180deg,#6f8fc0 0%,#b9c7dc 45%,#c9c3b8 65%,#5f8a3a 100%)"></div>
    <span class="badge type" style="left:106px">RENTALS</span><span class="badge new" style="left:200px">NEW OFFER</span>
    <h3 class="listing-title">SED UT PERSPICIATIS</h3>
    <p class="listing-price">$ 2,000 / year</p>
    <p class="listing-desc">Lorem ipsum dolor sit amet, consectetur adipiscing elit, sed do eiusmod tempor incididunt ut labore</p>
    <div class="listing-specs">
      <svg width="18" height="12" viewBox="0 0 18 12"><path fill="#111" d="M0 0h2v6h16v6h-2V9H2v3H0zM3 3h3v3H3zM7 3h9a2 2 0 0 1 2 2v1H7z"/></svg><span>1</span>
      <svg width="16" height="14" viewBox="0 0 16 14"><path fill="#111" d="M1 7h14v3a3 3 0 0 1-3 3H4a3 3 0 0 1-3-3zM2 1h3v2H4v4H2z"/></svg><span>1</span>
      <svg width="16" height="16" viewBox="0 0 16 16"><path fill="#111" d="M0 5h11v11H0zm2 2v7h7V7zM5 0h11v11h-4V9h2V2H7v2H5z"/></svg><span>120 ft2</span>
    </div>
  </article>

  <article class="listing-card" style="left:446px">
    <div class="listing-photo" role="img" aria-label="Modern two-storey home with stone and timber facade" style="background:linear-gradient(180deg,#a9a9a9 0%,#d9d8d4 45%,#6b5a4b 75%,#4c4c4c 100%)"></div>
    <span class="badge type" style="left:106px">RENTALS</span><span class="badge new" style="left:200px">NEW OFFER</span>
    <h3 class="listing-title">SED UT PERSPICIATIS</h3>
    <p class="listing-price">$ 2,000 / year</p>
    <p class="listing-desc">Lorem ipsum dolor sit amet, consectetur adipiscing elit, sed do eiusmod tempor incididunt ut labore</p>
    <div class="listing-specs">
      <svg width="18" height="12" viewBox="0 0 18 12"><path fill="#111" d="M0 0h2v6h16v6h-2V9H2v3H0zM3 3h3v3H3zM7 3h9a2 2 0 0 1 2 2v1H7z"/></svg><span>1</span>
      <svg width="16" height="14" viewBox="0 0 16 14"><path fill="#111" d="M1 7h14v3a3 3 0 0 1-3 3H4a3 3 0 0 1-3-3zM2 1h3v2H4v4H2z"/></svg><span>1</span>
      <svg width="16" height="16" viewBox="0 0 16 16"><path fill="#111" d="M0 5h11v11H0zm2 2v7h7V7zM5 0h11v11h-4V9h2V2H7v2H5z"/></svg><span>120 ft2</span>
    </div>
  </article>

  <article class="listing-card" style="left:781px">
    <div class="listing-photo" role="img" aria-label="Blue weatherboard house with stone path and lawn at dusk" style="background:linear-gradient(180deg,#4e5a6e 0%,#5f6f8c 40%,#8a7a5c 62%,#4f7a33 100%)"></div>
    <span class="badge type" style="left:106px">RENTALS</span><span class="badge new" style="left:200px">NEW OFFER</span>
    <h3 class="listing-title">SED UT PERSPICIATIS</h3>
    <p class="listing-price">$ 2,000 / year</p>
    <p class="listing-desc">Lorem ipsum dolor sit amet, consectetur adipiscing elit, sed do eiusmod tempor incididunt ut labore</p>
    <div class="listing-specs">
      <svg width="18" height="12" viewBox="0 0 18 12"><path fill="#111" d="M0 0h2v6h16v6h-2V9H2v3H0zM3 3h3v3H3zM7 3h9a2 2 0 0 1 2 2v1H7z"/></svg><span>1</span>
      <svg width="16" height="14" viewBox="0 0 16 14"><path fill="#111" d="M1 7h14v3a3 3 0 0 1-3 3H4a3 3 0 0 1-3-3zM2 1h3v2H4v4H2z"/></svg><span>1</span>
      <svg width="16" height="16" viewBox="0 0 16 16"><path fill="#111" d="M0 5h11v11H0zm2 2v7h7V7zM5 0h11v11h-4V9h2V2H7v2H5z"/></svg><span>120 ft2</span>
    </div>
  </article>
</section>

<section class="insights">
  <h2 class="section-title" style="top:2194px">INSIGHTS</h2>

  <article class="insight" style="left:206px;top:2290px">
    <div class="insight-photo" role="img" aria-label="Agent with laptop advising a couple at a table" style="background:linear-gradient(135deg,#b9a48a 0%,#dfe3ea 40%,#c24a3a 75%,#8a6b4c 100%)"></div>
    <p class="insight-label">LOREM IPSUM</p>
    <h3 class="insight-title">SED UT PERSPICIATIS</h3>
    <p class="insight-text">Lorem ipsum dolor sit amet, consectetur adipiscing elit, sed do eiusmod tempor incididunt ut labore et dolore magna aliqua. Ut enim ad minim veniam, quis nostrud exercitation ullamco</p>
    <p class="insight-price">$699.000</p>
  </article>

  <article class="insight" style="left:615px;top:2290px">
    <div class="insight-photo" role="img" aria-label="House model, keys, gavel and chart on a white desk" style="background:linear-gradient(135deg,#8a4a3a 0%,#e9ecef 35%,#f2f3f4 60%,#c9a45a 80%,#3d7fb0 100%)"></div>
    <p class="insight-label">LOREM IPSUM</p>
    <h3 class="insight-title">SED UT PERSPICIATIS</h3>
    <p class="insight-text">Lorem ipsum dolor sit amet, consectetur adipiscing elit, sed do eiusmod tempor incididunt ut labore et dolore magna aliqua. Ut enim ad minim veniam, quis nostrud exercitation ullamco</p>
    <p class="insight-price">$699.000</p>
  </article>

  <article class="insight" style="left:206px;top:2862px">
    <div class="insight-photo" role="img" aria-label="Hand using a calculator beside house models and coins" style="background:linear-gradient(135deg,#9c8a70 0%,#d9b98c 40%,#eef0e6 60%,#b98c58 100%)"></div>
    <p class="insight-label">LOREM IPSUM</p>
    <h3 class="insight-title">SED UT PERSPICIATIS</h3>
    <p class="insight-text">Lorem ipsum dolor sit amet, consectetur adipiscing elit, sed do eiusmod tempor incididunt ut labore et dolore magna aliqua. Ut enim ad minim veniam, quis nostrud exercitation ullamco</p>
    <p class="insight-price">$699.000</p>
  </article>

  <article class="insight" style="left:615px;top:2862px">
    <div class="insight-photo" role="img" aria-label="Hand holding a key with a small house keyring against a blurred garden" style="background:linear-gradient(135deg,#d8c6a2 0%,#c9b08a 40%,#6f8a5a 75%,#2f5a48 100%)"></div>
    <p class="insight-label">LOREM IPSUM</p>
    <h3 class="insight-title">SED UT PERSPICIATIS</h3>
    <p class="insight-text">Lorem ipsum dolor sit amet, consectetur adipiscing elit, sed do eiusmod tempor incididunt ut labore et dolore magna aliqua. Ut enim ad minim veniam, quis nostrud exercitation ullamco</p>
    <p class="insight-price">$699.000</p>
  </article>
</section>

<footer class="site-footer">
  <p class="footer-heading" style="left:178px">SED UT PERSPICIATIS UNDE OMNIS ISTE NATUS<br>ERROR SIT VOLUPTATEM:</p>
  <div class="footer-contact">
    <p>Phone: 188-555-014</p>
    <p>Email: hello@peckfordrealty.example</p>
    <p>Fax: 1235550199</p>
  </div>
  <p class="copyright">©Copyrights 2021 Peckford Realty &nbsp;|&nbsp;&nbsp; All Rights Reserved</p>

  <p class="footer-heading" style="left:639px">SED UT PERSPICIATIS UNDE OMNIS ISTE NATUS<br>ERROR SIT VOLUPTATEM:</p>
  <div class="field" style="left:639px;top:146px;width:186px;height:32px">Name</div>
  <div class="field" style="left:639px;top:189px;width:186px;height:32px">Email</div>
  <div class="field" style="left:639px;top:232px;width:186px;height:31px">Subject</div>
  <div class="field" style="left:837px;top:146px;width:186px;height:117px">Message</div>
  <div class="submit">SUBMIT</div>
</footer>

</body>
</html>
```